Brackwell + Sorrent Architecture Ltd Stationary rebrand Lead designer to create a fresh clean modern...

We have recieved a great new logo design and now we are after a consistant fresh and modern stationary to match the new design. Business card design, Letter Head design, presentatnion folders and other stationery within the package. I have also added some of our existing layouts for presentation we would like updating with the new look, We would like a clean modern fresh design that looks visually pleasing on the page. we cant wait to see what you come up with!!!!

Target Market(s)

young professionals and middle age clients

Industry/Entity Type

Architect

Contact Information for Business Card

i have uploarded our orginal business card that has all the details attached.

Font styles to use
Sans Serif

Colors
000000
ffffff
d3d3d3

Requirements
Must have
• Logo and our contact information
Nice to have
• white sape around the card to give a clean look.

```html
<!DOCTYPE html>
<html lang="en">
<head>
<meta charset="utf-8">
<title>Brackwell + Sorrent Architecture – Business Card</title>
<link href="https://fonts.googleapis.com/css2?family=Poppins:wght@400;500&display=swap" rel="stylesheet">
<style>
  :root {
    --black: #000000;
    --white: #ffffff;
    --light-grey: #d3d3d3;
    --stage: #e4e4e4;
    --text-grey: #555555;
    --muted-grey: #b5b5b5;
    --pattern-dark: #0b0b0b;
    --pattern-mid: #1c1c1c;
  }
  * { margin: 0; padding: 0; box-sizing: border-box; }
  html, body { width: 1200px; height: 1200px; overflow: hidden; }
  body {
    background: var(--stage);
    font-family: "Poppins", Arial, sans-serif;
    position: relative;
  }
  .card {
    position: absolute;
    left: 262px;
    width: 686px;
    height: 392px;
    box-shadow: 0 2px 6px rgba(0,0,0,0.12);
  }
  .card--front { top: 165px; background: var(--white); }
  .card--back { top: 653px; overflow: hidden; }

  /* Brand block */
  .brand {
    position: absolute;
    left: 78px;
    top: 128px;
    width: 242px;
    text-align: center;
    color: var(--black);
    font-weight: 500;
  }
  .brand__square {
    width: 44px; height: 44px;
    background: var(--black);
    margin: 0 auto 20px;
  }
  .brand__name {
    font-size: 17px;
    letter-spacing: 2px;
    line-height: 1;
    white-space: nowrap;
  }
  .brand__sub {
    font-size: 10px;
    letter-spacing: 9px;
    margin-top: 8px;
    margin-right: -9px;
    line-height: 1;
  }

  /* Contact */
  .contact {
    position: absolute;
    left: 355px;
    top: 82px;
    color: var(--text-grey);
    font-size: 16.5px;
    line-height: 22px;
  }
  .contact__name {
    color: var(--black);
    font-size: 26px;
    font-weight: 500;
    line-height: 32px;
  }
  .contact__role {
    color: var(--muted-grey);
    font-size: 17px;
    line-height: 20px;
    margin-bottom: 24px;
  }
  .contact__block { margin-bottom: 20px; }

  /* Footer band */
  .footer-rule {
    position: absolute;
    bottom: 0;
    height: 10px;
    background: var(--black);
  }
  .footer-rule--left { left: 0; width: 348px; }
  .footer-rule--right { right: 0; width: 52px; }
  .web-tab {
    position: absolute;
    left: 351px;
    bottom: 0;
    width: 281px;
    height: 31px;
    background: var(--black);
    color: var(--white);
    font-size: 16.5px;
    letter-spacing: 0.6px;
    line-height: 31px;
    text-align: center;
  }

  /* Back */
  .back-pattern {
    position: absolute;
    inset: 0;
    background: linear-gradient(160deg, var(--pattern-mid), var(--pattern-dark));
  }
  .back-brand {
    position: absolute;
    right: 42px;
    bottom: 30px;
    display: flex;
    align-items: center;
    gap: 10px;
    color: var(--white);
    font-weight: 500;
    font-size: 13px;
    letter-spacing: 1.5px;
  }
  .back-brand__square {
    width: 26px; height: 26px;
    border: 5px solid var(--white);
  }
</style>
</head>
<body>
  <section class="card card--front">
    <div class="brand">
      <div class="brand__square"></div>
      <div class="brand__name">BRACKWELL + SORRENT</div>
      <div class="brand__sub">ARCHITECTURE</div>
    </div>

    <div class="contact">
      <div class="contact__name">Thomas Brackwell</div>
      <div class="contact__role">Director</div>
      <div class="contact__block">
        42 Halden Road<br>
        Marwick 7710<br>
        PO Box 5138, Marwick 7745
      </div>
      <div>
        P. 03 555 0142<br>
        M. 0270 555 218<br>
        thomas@bsarchitecture.co.nz
      </div>
    </div>

    <div class="footer-rule footer-rule--left"></div>
    <div class="web-tab">www.bsarchitecture.co.nz</div>
    <div class="footer-rule footer-rule--right"></div>
  </section>

  <section class="card card--back">
    <div class="back-pattern" role="img" aria-label="Dark repeating brand pattern filling the back of the card"></div>
    <div class="back-brand">
      <div class="back-brand__square"></div>
      <span>BRACKWELL + SORRENT</span>
    </div>
  </section>
</body>
</html>
```